Bauzaunbanner für Fertigung und Montagen von Metallbau- und Stahlkonstruktionen
Zielgruppe
Fertigung und Montagen von Metallbau- und Stahlkonstruktionen
Aufgabenstellung
Außenwerbung an unserem Produktionsstandort (große halle); Blickdistanz ca. 50m; Stellengesuch 'Monteure' (w/m/d); Breite ca. 5.000mm; einfache (Bild-)Botschaft

```html
<!DOCTYPE html>
<html lang="de">
<head>
<meta charset="utf-8">
<title>Bauzaunbanner – Monteure gesucht</title>
<link rel="stylesheet" href="https://fonts.googleapis.com/css2?family=Barlow+Condensed:wght@500;600;700&display=swap">
<style>
  :root {
    --canvas-bg: #ebebeb;
    --banner-white: #ffffff;
    --brand-blue: #1070bb;
    --ink-dark: #262626;
    --photo-dark: #4a5260;
    --photo-mid: #8a929c;
    --photo-light: #c9ccd0;
  }
  html, body {
    margin: 0;
    padding: 0;
    width: 1200px;
    height: 1200px;
    overflow: hidden;
    background: var(--canvas-bg);
  }
  .banner {
    position: absolute;
    left: 225px;
    top: 510px;
    width: 750px;
    height: 179px;
    display: block;
    font-family: "Barlow Condensed", "Arial Narrow", sans-serif;
  }
  .banner-bg { fill: var(--banner-white); }
  .diagonal-band { fill: var(--brand-blue); }
  .headline-job { fill: var(--brand-blue); font-weight: 700; font-size: 61px; }
  .headline-gender { fill: var(--brand-blue); font-weight: 500; font-size: 45px; }
  .divider { fill: var(--brand-blue); }
  .headline-wanted { fill: var(--ink-dark); font-weight: 700; font-size: 62px; }
  .trade-line { fill: var(--ink-dark); font-weight: 700; font-size: 30px; }
  .url-pill { fill: var(--banner-white); }
  .url-text { fill: var(--brand-blue); font-weight: 700; font-size: 18px; letter-spacing: 1px; }
  .company-mark { fill: none; stroke: var(--banner-white); stroke-width: 1.6; }
  .company-name { fill: var(--banner-white); font-weight: 600; font-size: 7.5px; letter-spacing: 0.3px; }
</style>
</head>
<body>
<svg class="banner" viewBox="0 0 750 179" xmlns="http://www.w3.org/2000/svg">
  <defs>
    <linearGradient id="photoTone" x1="0" y1="0" x2="1" y2="1">
      <stop offset="0" stop-color="#4a5260"/>
      <stop offset="0.45" stop-color="#8a929c"/>
      <stop offset="1" stop-color="#c9ccd0"/>
    </linearGradient>
  </defs>

  <rect class="banner-bg" x="0" y="0" width="750" height="179"/>

  <polygon points="0,0 250,0 395,179 0,179" fill="url(#photoTone)"
           role="img" aria-label="Foto: lächelnder Metallbauer mit hochgeklapptem Schweißhelm in einer Produktionshalle"/>

  <polygon class="diagonal-band" points="235,0 269,0 413,179 378,179"/>

  <g class="company-signature">
    <circle class="company-mark" cx="30" cy="29" r="12"/>
    <text class="company-name" x="48" y="24">METALLBAU</text>
    <text class="company-name" x="48" y="31">KESSNER</text>
    <text class="company-name" x="48" y="38">GMBH</text>
  </g>

  <g class="web-address">
    <rect class="url-pill" x="170" y="150" width="177" height="22" rx="11"/>
    <text class="url-text" x="258.5" y="167" text-anchor="middle">WWW.KESSNER.DE</text>
  </g>

  <text x="343" y="60">
    <tspan class="headline-job">MONTEURE</tspan>
    <tspan class="headline-gender" dx="6">(m/w/d)</tspan>
  </text>

  <rect class="divider" x="351" y="76" width="399" height="4"/>

  <text class="headline-wanted" x="619" y="140" text-anchor="middle">GESUCHT</text>
  <text class="trade-line" x="619" y="169" text-anchor="middle">Metall- &amp; Stahlbau</text>
</svg>
</body>
</html>
```